□今後強化していきたい点
・新規顧客集客
・既存顧客への情報発信
・求人

▶ターゲット
<現在>
20~30代(メイン)
40~60代まで幅広く
会社員
主婦
お子様連れ
学生
女性7:男性3

<今後>
20~30代(メイン)
会社員
主婦
学生
女性7:男性3
強化したい項目:新規顧客増、来店頻度増

-----------------------------------

<現サイトの問題点>
・更新の利便性
・情報量(専門性)
・携帯での導線

<最大の要望は?>
①デザイン性の向上
②操作性の向上
③店舗の強みの打ち出し

<ホームページに期待する効果>
・求職者向け
・既存顧客むけ
・求職者向け

◆サイトマップ
1.TOP
∟2.サロンコンセプト★
∟3.1店舗目情報ページ
∟4.2店舗目情報ページ
∟5.スタッフ一覧★
∟6.スタッフ詳細
∟7.スタイルギャラリー一覧★
∟8.スタイルギャラリー詳細
∟9.メニュー一覧
∟10.プロダクト一覧
∟11.求人情報①店舗について、先輩スタッフインタビューなど★
∟12.求人情報②募集要項★
∟13.ニュース一覧★
∟14.ニュース詳細
∟15.ブログ一覧★
∟16.ブログ詳細
∟17.トリートメント、ヘアケアについて★

※★がついている項目についてはTOPページへ入り口を配置頂きたい項目になります。
(よりよい構成がございましたら、どうぞご自由にご提案ください。)

【参考サイト】
https://kiro-lashworks.com/

http://dunmoth.com/
→デザインをされる際に、こちらのサイトのように
スタッフ紹介部分を写真の切り抜きで構成をお願い致します。

https://roi-te.com/

■デザインのテイスト
カジュアル、ナチュラル、モダン
シンプルでわかりやすさは残しつつ、
ワンポイントでイラストや画像の切り抜き、飾り枠などを使用するなど、
センスよく少しにぎやかな雰囲気にしたいと考えております。

■補足説明
【ダミーテキストについて】
・極力サイト内の文章を配置下さい。
ブログ・ニュースのタイトル部分などは
「タイトルが入ります。」で大丈夫です。
「ここに文章が入ります。ここに文章が入ります。」などの
同じ文章を繰り返したダミー文章は極力使用しないようお願いいたします。
また、フォントに関しては読み込み速度等の観点から、
ウェブフォントの使用は避けて頂けますと幸いです。

※業務への支障がでる可能性がございますので、
電話でのご連絡はご遠慮頂いております。
http://mil-e-vo.tokyo/salon
茶系、緑系、ベースカラーは白、 差し色はブラウン系かグリーン系の色 グレーの使用はご遠慮頂けますと幸いです。
◆素材について
①素材として必要なものがある場合には、ミラフォトバンク画像をご使用ください。
その際、定期契約でダウンロード出来る画像のみを使用してください。
ミラフォトバンク以外の素材を使用する際には、
必ず無料で提供いただける物のみご使用ください。
ミラフォトバンク: https://pics.mirafoto.com/jp/

【院内写真、ロゴについて】
院内写真などの素材については下記URLよりダウンロードをお願い致します。
https://58.sendcrate.nu/4417-f0a9d2e61b7c34a8e5d90b2c1f6a7e4d5
https://58.sendcrate.nu/4417-d83e0c5a92f14b6e7a1c08d5e3b9f2c71
https://58.sendcrate.nu/4417-k2a9e5c710b6d4f38c1e9a07d6b4e5f93
更に多くのデザインを見たいと考えておりますので、
募集期間を延長させて頂きます。

どうぞ自由な発想でのご提案をお待ちしております。

以上、何卒宜しくお願い致します。
更に多くのデザインを見たいと考えておりますので、
募集期間を延長させて頂きます。

どうぞ自由な発想でのご提案をお待ちしております。

以上、何卒宜しくお願い致します。

サロンの雰囲気と合致していたため

この度はご提案を頂きありがとうございました。

```html
<!DOCTYPE html>
<html lang="ja">
<head>
<meta charset="utf-8">
<title>mil e vo | 365日「毎日が記念日」</title>
<link rel="stylesheet" href="https://fonts.googleapis.com/css2?family=M+PLUS+Rounded+1c:wght@400;700;800&family=Zilla+Slab:wght@700&display=swap">
<style>
:root{
  --green:#a9d08e;
  --green-soft:#c9e3b6;
  --green-deep:#7fa968;
  --brown:#4e3322;
  --brown-mid:#6b4a32;
  --cream:#fbf8f1;
  --white:#ffffff;
  --text:#4a3526;
  --photo-wood:#b58d67;
  --photo-room:#e7e2d6;
}
*{box-sizing:border-box;margin:0;padding:0}
html,body{width:1200px;height:5048px;overflow:hidden}
body{position:relative;background:var(--white);color:var(--text);font-family:"M PLUS Rounded 1c",sans-serif;font-size:17px;line-height:1.75}
.abs{position:absolute}
.green{background:var(--green)}
.photo{position:absolute}
.heading{position:absolute;font-family:"Zilla Slab",serif;font-weight:700;color:var(--brown);font-size:64px;line-height:1;text-align:center;width:100%;z-index:2}
.btn{position:absolute;border:2px solid var(--brown);background:var(--white);color:var(--brown);font-size:15px;text-align:center;line-height:38px;height:42px;border-radius:4px}
.more{position:absolute;color:var(--white);font-size:20px}

/* header */
.logo{position:absolute;left:28px;top:14px;font-weight:800;font-size:34px;color:var(--brown);display:flex;align-items:center;gap:10px}
.logo i{display:block;width:18px;height:18px;background:var(--brown);border-radius:50%}
.menu{position:absolute;right:0;top:0;width:68px;height:68px;background:var(--brown);color:var(--white);font-size:11px;text-align:center;padding-top:14px}
.menu span{display:block;width:30px;height:3px;background:var(--white);margin:4px auto}
.hero-title{position:absolute;left:60px;top:270px;font-weight:800;font-size:96px;color:var(--brown);line-height:1;z-index:2}
.hero-sub{position:absolute;left:90px;top:400px;font-size:26px;font-weight:700;color:var(--brown)}
.hero-copy{position:absolute;left:90px;top:460px;width:330px;font-size:16px;line-height:1.9}

/* concept */
.concept-list{position:absolute;left:580px;top:880px;width:560px;list-style:none}
.concept-list li{position:relative;padding-left:50px;margin-bottom:34px;font-size:16px}
.concept-list li::before{content:"";position:absolute;left:0;top:2px;width:30px;height:30px;border:2px solid var(--brown);border-radius:50%}

/* staff */
.staff-name{position:absolute;font-size:14px;font-weight:700;color:var(--brown);letter-spacing:.08em}

/* recruit */
.recruit-text{position:absolute;left:520px;top:2760px;width:640px;font-size:16px}
.req{position:absolute;left:90px;top:3090px;width:620px;font-size:16px;line-height:1.9}
.req h3{font-size:17px;margin-left:190px;margin-bottom:10px}

/* news */
.news-row{position:absolute;left:100px;width:1000px;height:60px;border-bottom:1px solid var(--white);display:flex;align-items:center;gap:28px;color:var(--brown);font-size:20px}
.tag{background:var(--brown);color:var(--white);font-size:14px;padding:2px 14px;border-radius:3px}

/* blog */
.card{position:absolute;width:300px}
.card .thumb{height:230px;background:linear-gradient(160deg,#eef2e6,#7fa968)}
.card p{background:var(--white);text-align:center;font-size:20px;padding:10px 0;line-height:1.5}

/* kodawari */
.kodawari-panel{position:absolute;left:480px;top:4660px;width:720px;height:290px;background:var(--green)}
.kodawari-title{position:absolute;left:600px;top:4570px;font-size:56px;font-weight:800;color:var(--brown);line-height:1.2;z-index:2}
.kodawari-text{position:absolute;left:520px;top:4690px;width:640px;font-size:16px}
.reserve{position:absolute;left:0;top:4900px;width:110px;height:44px;background:var(--white);border:2px solid var(--brown);color:var(--brown);font-size:15px;text-align:center;line-height:40px}
footer{position:absolute;left:0;top:4964px;width:1200px;height:84px;background:var(--brown);color:var(--white);text-align:center;line-height:84px;font-size:20px}
</style>
</head>
<body>

<!-- header / hero -->
<div class="abs green" style="left:0;top:0;width:1200px;height:120px;opacity:.55"></div>
<div class="logo"><i></i>mil e vo</div>
<div class="menu"><span></span><span></span><span></span>MENU</div>
<div class="photo" role="img" aria-label="サロン入口のガラス扉と観葉植物" style="left:460px;top:140px;width:740px;height:520px;background:linear-gradient(135deg,#3c3a33,#7d8a6a 55%,#e9eee4)"></div>
<h1 class="hero-title">mil e vo</h1>
<p class="hero-sub">365日「毎日が記念日」</p>
<p class="hero-copy">【mil e vo】とはフランス語で一歩一歩に寄り添う意味です。一日一日を大切にしながら一歩一歩豊かに歩んでいただくというコンセプトから、この名前を付けました。服も気分も変わる日を、ぜひお気軽にご来店ください。</p>

<!-- concept -->
<div class="abs green" style="left:420px;top:780px;width:780px;height:600px"></div>
<div class="photo" role="img" aria-label="木の棚に並ぶ観葉植物と雑貨" style="left:0;top:740px;width:560px;height:340px;background:linear-gradient(120deg,var(--photo-room),var(--photo-wood))"></div>
<h2 class="heading" style="left:620px;top:800px;width:auto;text-align:left">concept</h2>
<ul class="concept-list">
  <li>365日「毎日が記念日」をセットにお客様の人生を彩るご提案をします。</li>
  <li>「また通いたくなるサロン」「髪の毛が嬉しいサロン」であることを大切にし、お客様1人ひとりに寄り添う施術とサービスをご提供いたします。</li>
  <li>カラー剤にもこだわり、オーガニックや植物由来の毛がつややかになるアルカリ無しの薬剤を使用。お客様の髪の毛に合わせて施術しています。</li>
  <li>2店舗展開をしております。</li>
</ul>
<div class="photo" role="img" aria-label="葉の飾りイラスト" style="left:90px;top:1180px;width:170px;height:70px;background:var(--green-soft);border-radius:40px"></div>
<div class="btn" style="left:650px;top:1320px;width:220px">〇〇店舗はこちら</div>
<div class="btn" style="left:930px;top:1320px;width:220px">〇〇店舗はこちら</div>

<!-- staff -->
<div class="abs green" style="left:0;top:1472px;width:1200px;height:90px"></div>
<h2 class="heading" style="top:1480px">Staff</h2>
<div class="photo" role="img" aria-label="スタッフ切り抜き写真・黒いワンピースの女性" style="left:220px;top:1590px;width:180px;height:420px;background:linear-gradient(180deg,var(--green-soft),var(--brown-mid));border-radius:80px 80px 20px 20px"></div>
<p class="staff-name" style="left:160px;top:1840px">NAHO</p>
<div class="photo" role="img" aria-label="スタッフ切り抜き写真・白いワンピースの女性" style="left:500px;top:1570px;width:220px;height:450px;background:linear-gradient(180deg,var(--green-soft),#e8e0d4);border-radius:90px 90px 20px 20px"></div>
<p class="staff-name" style="left:600px;top:1870px">RIKA</p>
<div class="photo" role="img" aria-label="スタッフ切り抜き写真・ニットとオレンジのパンツの女性" style="left:860px;top:1580px;width:180px;height:430px;background:linear-gradient(180deg,#cfe0e6,#d98f5c);border-radius:80px 80px 20px 20px"></div>
<p class="staff-name" style="left:1040px;top:1770px">EMI</p>

<!-- style gallery -->
<h2 class="heading" style="top:2058px">Style Gallery</h2>
<div class="abs green" style="left:0;top:2140px;width:1200px;height:340px"></div>
<div class="photo" role="img" aria-label="スタイル写真・ボブヘアの女性" style="left:60px;top:2180px;width:280px;height:220px;background:linear-gradient(160deg,#f4efe8,#8c6a50)"></div>
<div class="photo" role="img" aria-label="スタイル写真・ミディアムヘアの女性" style="left:380px;top:2150px;width:440px;height:290px;background:linear-gradient(160deg,#f5f1ea,#6e5240);border:6px solid var(--white)"></div>
<div class="photo" role="img" aria-label="スタイル写真・ロングヘアの女性" style="left:860px;top:2180px;width:300px;height:220px;background:linear-gradient(160deg,#f4efe8,#5b4130)"></div>
<div class="btn" style="left:900px;top:2440px;width:240px;height:34px;line-height:30px;font-size:13px;background:var(--green);color:var(--white);border-color:var(--white)">スタイル一覧はこちら ▶</div>

<!-- recruit -->
<h2 class="heading" style="top:2530px">Recruit</h2>
<div class="abs green" style="left:480px;top:2720px;width:720px;height:320px"></div>
<div class="photo" role="img" aria-label="サロン店内の窓辺と椅子" style="left:0;top:2640px;width:460px;height:340px;background:linear-gradient(120deg,#f2eee6,#a7714b)"></div>
<p class="recruit-text">【mil e vo】とはフランス語で一歩一歩共に歩むという意味です。一日一日を大切にしながら一歩一歩豊かに歩んでいただくというコンセプトのように、スタッフの皆様も一歩一歩を大切に、スタッフ全員が笑顔の絶えない方を目指しています。美容師に必要なことは全て【mil e vo】で覚えられます！是非私たちと一緒に働きましょう！</p>
<div class="btn" style="left:860px;top:2920px;width:300px;height:34px;line-height:30px;font-size:13px;background:var(--green);color:var(--white);border-color:var(--white)">先輩スタッフのインタビューはこちら ▶</div>
<div class="abs green" style="left:0;top:3040px;width:740px;height:320px"></div>
<div class="photo" role="img" aria-label="木の動物の置物と小物" style="left:740px;top:3060px;width:460px;height:280px;background:linear-gradient(120deg,#efe9df,#7d6a55)"></div>
<div class="req">
  <h3>募集要項</h3>
  <p>職種：アシスタント　¥178,000～/スタイリスト　経験に応じて<br>勤務時間：10:00～20:00<br>休日：週休2日制（月4日以上）/夏季冬季休暇あり<br>待遇：雇用保険・交通費支給・講習費・ウィッグ代等補助<br>その他：社会保険完備/各店舗可/制服貸与/ヘアケア割引の制度有<br><br>※サロン見学随時受付中お気軽にお問い合わせください</p>
</div>

<!-- news -->
<div class="abs green" style="left:0;top:3440px;width:1200px;height:500px"></div>
<h2 class="heading" style="top:3570px">NEWS</h2>
<div class="news-row" style="top:3680px"><span>2020/12/30</span><span class="tag">カテゴリ</span><span>タイトルが入ります。</span></div>
<div class="news-row" style="top:3752px"><span>2020/12/30</span><span class="tag">カテゴリ</span><span>タイトルが入ります。</span></div>
<div class="news-row" style="top:3824px"><span>2020/12/30</span><span class="tag">カテゴリ</span><span>タイトルが入ります。</span></div>
<p class="more" style="left:970px;top:3890px">▶ NEWS一覧</p>

<!-- blog -->
<div class="abs green" style="left:0;top:4080px;width:1200px;height:400px"></div>
<h2 class="heading" style="top:4010px">BLOG</h2>
<div class="card" style="left:70px;top:4100px"><div class="thumb" role="img" aria-label="観葉植物の鉢"></div><p>2020/12/30<br>タイトルが入ります。</p></div>
<div class="card" style="left:480px;top:4100px"><div class="thumb" role="img" aria-label="観葉植物の鉢"></div><p>2020/12/30<br>タイトルが入ります。</p></div>
<div class="card" style="left:880px;top:4100px"><div class="thumb" role="img" aria-label="観葉植物の鉢"></div><p>2020/12/30<br>タイトルが入ります。</p></div>
<p class="more" style="left:960px;top:4420px">▶ BLOG一覧</p>

<!-- kodawari -->
<div class="kodawari-panel"></div>
<div class="photo" role="img" aria-label="窓辺に並ぶ鉢植えの植物" style="left:0;top:4540px;width:480px;height:300px;background:linear-gradient(120deg,#f1eee6,#5e6b4a)"></div>
<h2 class="kodawari-title">\こだわりの薬剤/</h2>
<p class="kodawari-text">お客様の髪の毛を第一に考えたダメージレスな薬剤選定をしています。カラー剤にもこだわり、オーガニックや植物由来の毛がつややかになるヒアルロン酸入りのお客様の髪の毛に合わせて施術しています。オーガニックヘッドスパもお客様の髪質に合わせてアロマを選定し、安らぎのひと時をプレゼントいたします。</p>
<div class="reserve">RESERV</div>

<footer>Copyright (C) 2016 mil e vo All Rights Reserved.</footer>

</body>
</html>
```